Salon and Spa Distributor Business Card

Need a business card. We are are distributor in the salon and spa industry. We identify with natural beauty. Need a card with:
Company Name: Petal Haven"
Title: "President & CEO"
Address
Company Phone number
email
website
Tag Line:" The Professional Salon Source"

Industry/Entity Type

Business

Contact Information for Business Card

Name: Lena Morcott
Title: "President & CEO"
Address: 317 Birchfield Ln, Oakvane, NJ 07481
Company Phone number: 800-463-9152
email: lenamorcott@petalhaven-example.com
website: www.petalhaven-example.com

Requirements
Should not have
• No black backgrounds

```html
<!DOCTYPE html>
<html lang="en">
<head>
<meta charset="utf-8">
<title>Petal Haven – Business Card</title>
<link href="https://fonts.googleapis.com/css2?family=Questrial&display=swap" rel="stylesheet">
<style>
  :root {
    --stage: #ececec;
    --green-light: #62b848;
    --green: #3f9a3f;
    --green-deep: #2a7d3a;
    --ink: #2b2b2b;
    --paper: #ffffff;
  }
  * { box-sizing: border-box; margin: 0; padding: 0; }
  html, body { width: 1200px; height: 880px; overflow: hidden; }
  body {
    background: var(--stage);
    font-family: "Questrial", "Century Gothic", sans-serif;
    position: relative;
  }
  .card {
    position: absolute;
    width: 560px;
    height: 320px;
    border-radius: 22px;
    overflow: hidden;
    box-shadow: 0 10px 30px rgba(0,0,0,0.18);
  }
  /* Front */
  .card-front {
    left: 90px; top: 80px;
    background: radial-gradient(ellipse at 50% 40%, var(--green-light) 0%, var(--green) 55%, var(--green-deep) 100%);
    display: flex; align-items: center; justify-content: center;
  }
  .front-brand { display: flex; align-items: center; gap: 16px; color: var(--paper); }
  .brand-dot { width: 26px; height: 26px; border-radius: 50%; background: var(--paper); }
  .front-name { font-size: 44px; letter-spacing: 0.5px; }

  /* Back */
  .card-back { left: 550px; top: 480px; background: var(--paper); }
  .back-art { position: absolute; left: 0; top: 0; width: 320px; height: 320px; }
  .back-info { position: absolute; left: 292px; top: 38px; color: var(--ink); }
  .back-name { color: var(--green); font-size: 42px; line-height: 1; }
  .back-tagline { font-size: 14px; margin-top: 4px; margin-left: 14px; }
  .person { margin-top: 26px; }
  .person-name { color: var(--green); font-size: 18px; }
  .person-title { font-size: 14px; }
  .address { margin-top: 14px; font-size: 13px; line-height: 1.35; }
  .contacts { list-style: none; margin-top: 10px; font-size: 12.5px; }
  .contacts li { display: flex; align-items: center; gap: 7px; line-height: 1.55; }
  .contact-icon { width: 14px; height: 14px; flex: none; }
</style>
</head>
<body>
  <section class="card card-front">
    <div class="front-brand">
      <span class="brand-dot"></span>
      <span class="front-name">Petal Haven</span>
    </div>
  </section>

  <section class="card card-back">
    <svg class="back-art" viewBox="0 0 320 320" role="img" aria-label="Green illustration of a woman's profile with flowing hair and leaves">
      <defs>
        <linearGradient id="art-green" x1="0" y1="0" x2="1" y2="1">
          <stop offset="0" stop-color="#7cc553"/>
          <stop offset="0.6" stop-color="#4ea846"/>
          <stop offset="1" stop-color="#2a7d3a"/>
        </linearGradient>
      </defs>
      <path d="M0 80 C70 20 170 10 230 60 C300 120 320 230 300 320 L0 320 Z" fill="url(#art-green)"/>
    </svg>

    <div class="back-info">
      <h1 class="back-name">Petal Haven</h1>
      <p class="back-tagline">The Professional Salon Source</p>
      <div class="person">
        <p class="person-name">Lena Morcott</p>
        <p class="person-title">President &amp; CEO</p>
      </div>
      <p class="address">317 Birchfield Ln,<br>Oakvane, NJ 07481</p>
      <ul class="contacts">
        <li>
          <svg class="contact-icon" viewBox="0 0 14 14"><rect width="14" height="14" rx="2" fill="#3f9a3f"/><path d="M4 3.5 L5.5 3.5 L6.2 5.3 L5.3 6 C5.8 7 6.8 8 7.9 8.6 L8.6 7.7 L10.5 8.4 L10.5 10 C7 10.3 3.6 7 4 3.5 Z" fill="#fff"/></svg>
          800-463-9152
        </li>
        <li>
          <svg class="contact-icon" viewBox="0 0 14 14"><rect width="14" height="14" rx="2" fill="#3f9a3f"/><rect x="3" y="4" width="8" height="6" fill="none" stroke="#fff" stroke-width="1"/><path d="M3 4 L7 7.3 L11 4" fill="none" stroke="#fff" stroke-width="1"/></svg>
          lenamorcott@petalhaven-example.com
        </li>
        <li>
          <svg class="contact-icon" viewBox="0 0 14 14"><rect width="14" height="14" rx="2" fill="#3f9a3f"/><circle cx="7" cy="7" r="4" fill="none" stroke="#fff" stroke-width="1"/><ellipse cx="7" cy="7" rx="1.7" ry="4" fill="none" stroke="#fff" stroke-width="0.8"/><path d="M3 7 H11" stroke="#fff" stroke-width="0.8"/></svg>
          www.petalhaven-example.com
        </li>
      </ul>
    </div>
  </section>
</body>
</html>
```